Flyer for the Lumen 2025 Conference

I am looking to produce a flyer for our upcoming conference, Lumen 2025. This is an annual conference that we plan to publicize on social media. The ideal designer will create a flyer that is eye-catching and effectively communicates the key information. Please see attached our logo, speaker photo, and flyer content.

Target Market(s)

All demographics

Industry/Entity Type

Christian

Font styles to use
Sans Serif

Requirements
Should not have
• Cross, church

```html
<!DOCTYPE html>
<html lang="en">
<head>
<meta charset="utf-8">
<title>Lumen 2025 Conference Flyer</title>
<link href="https://fonts.googleapis.com/css2?family=Poppins:ital,wght@0,700;0,800;1,800&family=Oswald:wght@700&family=Open+Sans:ital,wght@0,400;0,600;1,600&display=swap" rel="stylesheet">
<style>
  :root {
    --page: #e6e2e2;
    --blue-top: #0058b2;
    --blue-mid: #0a3c86;
    --navy: #14153a;
    --orange: #f7931e;
    --white: #ffffff;
    --ink: #111111;
  }
  * { margin: 0; padding: 0; box-sizing: border-box; }
  html, body { width: 1200px; height: 1092px; overflow: hidden; background: var(--page); }
  .flyer {
    position: absolute; left: 54px; top: 0; width: 1092px; height: 1092px; overflow: hidden;
    background: linear-gradient(180deg, var(--blue-top) 0%, var(--blue-mid) 38%, var(--navy) 85%);
    font-family: "Open Sans", sans-serif; color: var(--white);
  }
  .abs { position: absolute; white-space: nowrap; }
  .backdrop-word {
    position: absolute; left: -40px; font-family: "Poppins", sans-serif; font-weight: 800;
    font-size: 200px; line-height: 1; color: rgba(255,255,255,0.035); letter-spacing: 4px;
  }
  .title { left: 44px; top: 44px; font-family: "Poppins", sans-serif; font-weight: 800;
    font-size: 206px; line-height: 1; color: var(--orange); letter-spacing: -2px; }
  .brand { left: 880px; top: 100px; display: flex; align-items: center; gap: 10px; }
  .brand-dot { width: 20px; height: 20px; border-radius: 50%; background: var(--orange); }
  .brand-name { font-weight: 600; font-size: 38px; color: var(--white); letter-spacing: 2px; }
  .year { left: 70px; top: 254px; font-family: "Oswald", sans-serif; font-weight: 700; font-size: 128px; line-height: 1; }
  .year-rule { left: 368px; top: 283px; width: 4px; height: 91px; background: var(--white); }
  .subtitle { left: 406px; top: 270px; font-family: "Poppins", sans-serif; font-style: italic; font-weight: 800;
    font-size: 46px; line-height: 60px; }
  .topic-label { left: 78px; top: 430px; font-family: "Poppins", sans-serif; font-weight: 700; font-size: 28px; color: var(--orange); }
  .topic-rule { left: 199px; top: 450px; width: 484px; height: 2px; background: var(--orange); }
  .topic { left: 72px; top: 464px; font-style: italic; font-weight: 600; font-size: 57px; letter-spacing: -0.5px; }
  .datetime-label { left: 58px; top: 590px; font-family: "Poppins", sans-serif; font-weight: 700; font-size: 37px; color: var(--orange); }
  .speaker-bar { left: 274px; top: 564px; width: 503px; height: 88px; background: var(--white); }
  .speaker-tag { left: 274px; top: 564px; width: 136px; height: 88px; background: var(--orange); }
  .speaker-arrow { left: 408px; top: 594px; }
  .speaker-label { left: 286px; top: 588px; font-family: "Poppins", sans-serif; font-weight: 700; font-size: 25px; }
  .speaker-name { left: 442px; top: 592px; font-size: 22px; color: var(--ink); }
  .session { font-weight: 600; font-size: 16px; line-height: 35px; }
  .location-box { left: 51px; top: 762px; width: 592px; height: 75px; border: 2px solid var(--orange); }
  .location-label { left: 66px; top: 772px; font-family: "Poppins", sans-serif; font-weight: 700; font-size: 39px; color: var(--orange); }
  .location-rule { left: 251px; top: 780px; width: 2px; height: 38px; background: var(--white); }
  .address { left: 269px; top: 778px; font-weight: 600; font-size: 16px; line-height: 20px; }
  .footer-band { left: 0; top: 937px; width: 1092px; height: 155px; background: var(--white); }
  .speaker-photo { left: 0; top: 0; }
  .app-button { left: 41px; top: 874px; width: 468px; height: 84px; border-radius: 18px; background: var(--orange);
    padding: 6px 0 0 25px; font-weight: 600; font-size: 27px; line-height: 34px; }
  .phone-icon { left: 60px; top: 990px; }
  .phone { left: 102px; top: 970px; font-weight: 600; font-size: 48px; color: var(--ink); }
  .contact-line { top: 1038px; font-size: 24px; color: var(--ink); }
  .contact-icon { top: 1043px; }
  .contact-sep { left: 287px; top: 1042px; width: 2px; height: 20px; background: var(--orange); }
</style>
</head>
<body>
<main class="flyer">
  <div class="backdrop-word" style="top:20px">LUMEN LUMEN</div>
  <div class="backdrop-word" style="top:230px">LUMEN LUMEN</div>
  <div class="backdrop-word" style="top:440px">LUMEN LUMEN</div>
  <div class="backdrop-word" style="top:650px">LUMEN LUMEN</div>
  <div class="backdrop-word" style="top:860px">LUMEN LUMEN</div>

  <h1 class="abs title">LUMEN</h1>

  <div class="abs brand"><span class="brand-dot"></span><span class="brand-name">HALDEN</span></div>

  <div class="abs year">2025</div>
  <div class="abs year-rule"></div>
  <div class="abs subtitle">A Prophetic<br>Conference</div>

  <div class="abs topic-label">TOPIC:</div>
  <div class="abs topic-rule"></div>
  <h2 class="abs topic">The Voice Of The Lord</h2>

  <div class="abs datetime-label">Date/Time</div>
  <div class="abs speaker-bar"></div>
  <div class="abs speaker-tag"></div>
  <svg class="abs speaker-arrow" width="16" height="26" viewBox="0 0 16 26"><polygon points="0,0 16,13 0,26" fill="#f7931e"/></svg>
  <div class="abs speaker-label">Speaker:</div>
  <div class="abs speaker-name">Prophet Elias Maren</div>

  <div class="abs session" style="left:66px;top:681px">Friday, December 26th,<br>6:30PM - 9:00PM</div>
  <div class="abs session" style="left:270px;top:682px">Saturday, December 27th,<br>5:30PM - 8:00PM</div>
  <div class="abs session" style="left:492px;top:681px">Sunday, December 29th,<br>4:30PM - 7:00PM</div>

  <div class="abs location-box"></div>
  <div class="abs location-label">Location</div>
  <div class="abs location-rule"></div>
  <div class="abs address">The Harborview Performing Arts Center 218<br>Linden Street Easton, Maine 04740</div>

  <div class="abs footer-band"></div>

  <svg class="abs speaker-photo" width="1092" height="1092" viewBox="0 0 1092 1092" role="img" aria-label="Portrait of the speaker in a blue suit and grey knit sweater">
    <defs>
      <linearGradient id="suitTone" x1="0" y1="0" x2="0" y2="1">
        <stop offset="0" stop-color="#4a3a36"/>
        <stop offset="0.35" stop-color="#1f6fd0"/>
        <stop offset="1" stop-color="#17509d"/>
      </linearGradient>
    </defs>
    <path fill="url(#suitTone)" d="M792 330 Q792 206 897 206 Q1005 206 1005 330 L1005 430 L1092 480 L1092 1092 L640 1092 L705 900 L745 620 L812 545 L792 430 Z"/>
  </svg>

  <div class="abs app-button">Download the HALDEN App<br>to stay updated on the event</div>

  <svg class="abs phone-icon" width="26" height="26" viewBox="0 0 24 24"><path fill="#f7931e" d="M6.6 10.8a15.1 15.1 0 0 0 6.6 6.6l2.2-2.2c.3-.3.7-.4 1-.2 1.1.4 2.3.6 3.6.6.6 0 1 .4 1 1V20c0 .6-.4 1-1 1C10.6 21 3 13.4 3 4c0-.6.4-1 1-1h3.5c.6 0 1 .4 1 1 0 1.3.2 2.5.6 3.6.1.3 0 .7-.2 1z"/></svg>
  <div class="abs phone">207 555 0147</div>

  <svg class="abs contact-icon" style="left:61px" width="20" height="20" viewBox="0 0 20 20"><g fill="none" stroke="#f7931e" stroke-width="1.6"><circle cx="10" cy="10" r="8.5"/><ellipse cx="10" cy="10" rx="3.8" ry="8.5"/><path d="M1.5 10h17M3 5.5h14M3 14.5h14"/></g></svg>
  <div class="abs contact-line" style="left:92px">www.halden.org</div>
  <div class="abs contact-sep"></div>
  <svg class="abs contact-icon" style="left:320px" width="20" height="16" viewBox="0 0 20 16"><rect width="20" height="16" rx="2" fill="#f7931e"/><path d="M1 2l9 7 9-7" fill="none" stroke="#fff" stroke-width="1.6"/></svg>
  <div class="abs contact-line" style="left:357px">contact@halden.org</div>
</main>
</body>
</html>
```